Business Card & Stationery for a Consulting Firm
Brivaro Consulting
Business Card & Stationery for a Consulting Firm - Consulting
Creative Brief
Professional
Kusumadewi Pramulyanto
Senior Consultant
Graha 4 Suite-M, Level 11 Jl Raya Pelangi Kav. 17-18 Taman Niaga Raya (TNR) Jakarta 12760
kusumadewi@brivaroconsulting-example.com
www.brivaroconsulting-example.com
Kusumadewi Kusumadewi
Dear All Designers, On the address, please omit the line "Taman Niaga Rayaa (TNR) and add Twitter: @brivaroconsulting and Facebook: Brivaro Consulting. Thank you

```html
<!DOCTYPE html>
<html lang="en">
<head>
<meta charset="utf-8">
<title>Brivaro Consulting – Business Card</title>
<link href="https://fonts.googleapis.com/css2?family=Montserrat:wght@400;600;700&family=Open+Sans:wght@400;600&display=swap" rel="stylesheet">
<style>
  :root {
    --navy: #1f3684;
    --navy-deep: #162a6b;
    --navy-light: #2b46a0;
    --ink: #2a2f3a;
    --muted: #5a6070;
    --paper: #ffffff;
    --paper-shade: #eef0f3;
    --stage: #e9e7e3;
  }
  * { box-sizing: border-box; margin: 0; padding: 0; }
  html, body { width: 1200px; height: 904px; overflow: hidden; }
  body {
    background: var(--stage);
    font-family: "Open Sans", Arial, sans-serif;
    display: flex;
    flex-direction: column;
    align-items: center;
    justify-content: center;
    gap: 40px;
  }
  .card {
    width: 700px;
    height: 400px;
    position: relative;
    box-shadow: 0 6px 18px rgba(0,0,0,0.18);
    overflow: hidden;
  }
  /* Back side */
  .card--back {
    background: radial-gradient(ellipse at 50% 45%, var(--navy-light), var(--navy) 55%, var(--navy-deep));
    display: flex;
    align-items: center;
    justify-content: center;
  }
  .brand {
    display: flex;
    align-items: center;
    gap: 12px;
    font-family: "Montserrat", Arial, sans-serif;
  }
  .brand__mark { width: 34px; height: 34px; }
  .brand__name { line-height: 1; font-weight: 700; }
  .brand__name span { display: block; }
  .card--back .brand__mark { background: var(--paper); }
  .card--back .brand__name { color: var(--paper); font-size: 30px; }
  .card--back .brand__name span + span { font-size: 20px; text-align: right; margin-top: 2px; }

  /* Front side */
  .card--front {
    background: linear-gradient(125deg, var(--paper) 55%, var(--paper-shade));
  }
  .card--front .brand {
    position: absolute;
    left: 55px;
    top: 92px;
    gap: 10px;
  }
  .card--front .brand__mark { background: var(--navy); width: 28px; height: 28px; }
  .card--front .brand__name { color: var(--navy); font-size: 24px; }
  .card--front .brand__name span + span { font-size: 16px; text-align: right; margin-top: 2px; }
  .brand__tagline {
    font-family: "Open Sans", Arial, sans-serif;
    font-size: 7px;
    color: var(--muted);
    line-height: 1.2;
    margin-left: 4px;
    align-self: flex-start;
    margin-top: 4px;
  }
  .person {
    position: absolute;
    left: 55px;
    top: 222px;
  }
  .person__name {
    font-family: "Montserrat", Arial, sans-serif;
    font-weight: 600;
    font-size: 19px;
    color: var(--navy);
  }
  .person__title {
    font-size: 14px;
    color: var(--ink);
    margin-top: 4px;
  }
  .contact {
    position: absolute;
    left: 395px;
    top: 88px;
    font-size: 13.5px;
    color: var(--ink);
    line-height: 19px;
    list-style: none;
  }
  .contact__address { margin-bottom: 2px; }
  .contact__item { display: flex; align-items: center; gap: 8px; }
  .contact__icon { width: 12px; height: 12px; flex: none; fill: var(--ink); }
  .contact__square { width: 11px; height: 11px; background: var(--ink); flex: none; }
</style>
</head>
<body>
  <section class="card card--back" aria-label="Card back">
    <div class="brand">
      <div class="brand__mark"></div>
      <div class="brand__name"><span>Brivaro</span><span>Consulting</span></div>
    </div>
  </section>

  <section class="card card--front" aria-label="Card front">
    <div class="brand">
      <div class="brand__mark"></div>
      <div class="brand__name"><span>Brivaro</span><span>Consulting</span></div>
      <div class="brand__tagline">Strategy<br>Growth<br>Results</div>
    </div>

    <div class="person">
      <p class="person__name">Kusumadewi Pramulyanto</p>
      <p class="person__title">Senior Consultant</p>
    </div>

    <ul class="contact">
      <li class="contact__address">Graha 4 Suite-M, Level 11<br>Jl Raya Pelangi Kav. 17-18<br>Jakarta 12760</li>
      <li class="contact__item">
        <svg class="contact__icon" viewBox="0 0 12 12"><path d="M2.5 0.5l2 2.5-1.2 1.3c.7 1.6 1.9 2.8 3.4 3.4L8 6.5l2.5 2-1 2.5C5 10.8 1.2 7 1 2.5z"/></svg>
        +62 21 5550148
      </li>
      <li class="contact__item">
        <svg class="contact__icon" viewBox="0 0 12 12"><rect x="3" y="0.5" width="6" height="11" rx="1"/><rect x="4" y="2" width="4" height="7" fill="#fff"/></svg>
        +62 81 5550273
      </li>
      <li class="contact__item">
        <svg class="contact__icon" viewBox="0 0 12 12"><rect x="0.5" y="2" width="11" height="8" rx="1"/><path d="M1 2.5l5 4 5-4" fill="none" stroke="#fff" stroke-width="1"/></svg>
        kusumadewi@brivaroconsulting-example.com
      </li>
      <li class="contact__item">
        <svg class="contact__icon" viewBox="0 0 12 12"><circle cx="6" cy="6" r="5.5"/><path d="M0.5 6h11M6 0.5c-2.5 3-2.5 8 0 11M6 0.5c2.5 3 2.5 8 0 11" fill="none" stroke="#fff" stroke-width="0.8"/></svg>
        www.brivaroconsulting-example.com
      </li>
      <li class="contact__item"><span class="contact__square"></span>@brivaroconsulting</li>
      <li class="contact__item"><span class="contact__square"></span>Brivaro Consulting</li>
    </ul>
  </section>
</body>
</html>
```